brenwick carpentry business card 2.0

id like to get some extra info added to my current business card ,but i am also open to a new design as well ,id like it to be a clean professional look
i have attached the original card files, i have also attached the crestline trades logo and licensed builder logo that id like to add to all the current info on the old card
also the color green is important as seen in the company logo

Industry/Entity Type

Carpentry

Colors
9bcb3c

```html
<!DOCTYPE html>
<html lang="en">
<head>
<meta charset="utf-8">
<title>Brenwick Carpentry business card</title>
<link rel="stylesheet" href="https://fonts.googleapis.com/css2?family=Montserrat:wght@400;500&family=Arimo:wght@400;700&display=swap">
<style>
  :root {
    --green: #9bcb3c;
    --ink: #111111;
    --paper: #ffffff;
    --night: #0a0a0a;
    --backdrop: #2d2d2d;
    --badge-blue: #1f4f8c;
  }
  * { box-sizing: border-box; margin: 0; padding: 0; }
  html, body { width: 1200px; height: 866px; overflow: hidden; }
  body {
    background: var(--backdrop);
    font-family: "Arimo", Arial, sans-serif;
    position: relative;
  }
  .card {
    position: absolute;
    top: 278px;
    width: 540px;
    height: 310px;
    overflow: hidden;
    box-shadow: 0 10px 30px rgba(0,0,0,.45);
  }
  .card::after {
    content: "";
    position: absolute;
    left: 0; right: 0; bottom: 0;
    height: 7px;
    background: var(--green);
  }
  .card--front { left: 40px; background: var(--paper); color: var(--ink); }
  .card--back  { left: 620px; background: var(--night); }

  .wordmark {
    display: flex;
    align-items: center;
    gap: 12px;
    font-family: "Montserrat", sans-serif;
    font-weight: 500;
    letter-spacing: 2px;
    text-transform: uppercase;
  }
  .wordmark__dot { width: 14px; height: 14px; background: var(--green); flex: none; }
  .card--front .wordmark { position: absolute; left: 34px; top: 34px; font-size: 30px; color: var(--ink); }
  .card--back .wordmark {
    position: absolute; left: 0; right: 0; top: 130px;
    justify-content: center; font-size: 34px; color: var(--paper);
  }

  .contact { position: absolute; left: 34px; top: 112px; }
  .contact__name { font-weight: 700; font-size: 22px; letter-spacing: .5px; text-transform: uppercase; }
  .contact__role { color: var(--green); font-size: 14px; margin-top: 3px; }
  .contact__list { list-style: none; margin-top: 14px; font-size: 15px; }
  .contact__list li { display: flex; align-items: center; gap: 10px; margin-bottom: 5px; }
  .contact__list svg { width: 16px; height: 16px; flex: none; }
  .contact__web { color: var(--green); }

  .badges { position: absolute; right: 30px; bottom: 26px; display: flex; align-items: flex-end; gap: 18px; }
  .badge--trades { width: 56px; height: 56px; background: var(--badge-blue); }
  .badge--licence { width: 76px; height: 76px; border-radius: 50%; background: var(--green); }
</style>
</head>
<body>
  <section class="card card--front" aria-label="Business card front">
    <div class="wordmark"><span class="wordmark__dot"></span>Brenwick Carpentry</div>

    <div class="contact">
      <p class="contact__name">Daniel Marsh</p>
      <p class="contact__role">Director / Brenwick Carpentry Ltd</p>
      <ul class="contact__list">
        <li>
          <svg viewBox="0 0 16 16" aria-hidden="true"><rect x="1" y="1" width="14" height="14" rx="2" fill="none" stroke="#9bcb3c" stroke-width="1.5"/><path d="M5 4c0 4 3 7 7 7l0-2-2-1-1 1c-1-.5-2-1.5-2.5-2.5l1-1-1-2z" fill="#9bcb3c"/></svg>
          02109876543
        </li>
        <li>
          <svg viewBox="0 0 16 16" aria-hidden="true"><rect x="1" y="3" width="14" height="10" fill="#9bcb3c"/><path d="M1 3l7 6 7-6" fill="none" stroke="#fff" stroke-width="1.2"/></svg>
          daniel@brenwickcarpentry.co.nz
        </li>
        <li>
          <svg viewBox="0 0 16 16" aria-hidden="true"><circle cx="8" cy="8" r="7" fill="#9bcb3c"/><path d="M1 8h14M8 1c-3 4-3 10 0 14M8 1c3 4 3 10 0 14" fill="none" stroke="#fff" stroke-width="1"/></svg>
          <span>www.<span class="contact__web">brenwickcarpentry</span>.co.nz</span>
        </li>
      </ul>
    </div>

    <div class="badges">
      <div class="badge--trades" role="img" aria-label="Crestline Trades membership badge"></div>
      <div class="badge--licence" role="img" aria-label="Licensed builder certification badge"></div>
    </div>
  </section>

  <section class="card card--back" aria-label="Business card back">
    <div class="wordmark"><span class="wordmark__dot"></span>Brenwick Carpentry</div>
  </section>
</body>
</html>
```